Visitenkarten für eine Hypnose-Praxis
Ich bin sehr zufrieden mit der professionellen Arbeitsweise von KOR2874. Es war immer ein netter Kontakt und meine Wünsche wurden schnell umgesetzt. Alle Vorschläge waren sehr kreativ und und so viel es mir leicht, eine schnelle Entscheidung zu treffen.
Zielgruppe
Wir sind eine Hypnose-Praxis und richten unser Angebot an Privatpersonen unterschiedlichen Alters, die therapeutische Unterstützung suchen.
Aufgabenstellung
Eher schlichtes und modernes Design

```html
<!DOCTYPE html>
<html lang="de">
<head>
<meta charset="utf-8">
<title>ruhepol – Visitenkarten</title>
<link rel="stylesheet" href="https://fonts.googleapis.com/css2?family=Montserrat:wght@300;400;500;700&display=swap">
<style>
  :root {
    --bg: #6f6f6f;
    --card: #ffffff;
    --card-shade: #ececec;
    --ink: #555555;
    --ink-soft: #4a4a4a;
    --green: #5aae5f;
    --green-dark: #3f9a4b;
    --teal: #3fb29c;
    --blue: #2f9fc6;
    --blue-dark: #1f6f9e;
  }
  * { box-sizing: border-box; margin: 0; padding: 0; }
  html, body { width: 1200px; height: 1017px; overflow: hidden; }
  body {
    background: var(--bg);
    font-family: "Montserrat", sans-serif;
    position: relative;
  }
  .card {
    position: absolute;
    width: 560px;
    height: 362px;
    background: var(--card);
    box-shadow: 0 10px 30px rgba(0,0,0,.35);
    overflow: hidden;
  }
  .card--front { left: 320px; top: 90px; }
  .card--back {
    left: 320px; top: 540px;
    background: linear-gradient(180deg, var(--card) 0%, var(--card-shade) 100%);
  }

  /* Front */
  .wordmark {
    position: absolute;
    left: 0; right: 0; top: 150px;
    display: flex; align-items: center; justify-content: center; gap: 18px;
  }
  .wordmark__square {
    width: 38px; height: 38px;
    border-radius: 7px;
    background: var(--green);
  }
  .wordmark__name {
    font-size: 64px;
    font-weight: 500;
    color: var(--ink);
    letter-spacing: 1px;
  }

  /* Back */
  .person {
    position: absolute;
    left: 120px; right: 20px; top: 56px;
    text-align: center;
    color: var(--ink-soft);
  }
  .person__name {
    font-size: 36px;
    font-weight: 300;
    letter-spacing: 6px;
    text-transform: uppercase;
  }
  .person__role {
    margin-top: 14px;
    font-size: 10.5px;
    font-weight: 500;
    letter-spacing: .6px;
    line-height: 1.5;
    text-transform: uppercase;
  }
  .contacts {
    position: absolute;
    left: 40px; top: 160px;
    list-style: none;
  }
  .contacts__item {
    display: flex; align-items: center; gap: 12px;
    height: 30px;
    font-size: 18px;
    font-weight: 300;
    color: var(--ink-soft);
    letter-spacing: .3px;
  }
  .contacts__icon {
    width: 26px; height: 24px;
    border-radius: 4px;
    display: flex; align-items: center; justify-content: center;
  }
  .contacts__icon--pin { background: var(--green); }
  .contacts__icon--mail { background: var(--green-dark); }
  .contacts__icon--web { background: var(--teal); }
  .contacts__icon--tel { background: transparent; }

  .hotline {
    position: absolute;
    left: 0; bottom: 0;
    width: 400px; height: 48px;
    background: linear-gradient(180deg, var(--blue) 0%, var(--blue-dark) 100%);
    border-top-right-radius: 10px;
    display: flex; align-items: center;
    padding-left: 80px;
    color: #fff;
    font-size: 19px;
    font-weight: 700;
    letter-spacing: .5px;
  }
  .hotline__tab {
    position: absolute;
    left: 14px; bottom: 0;
    width: 56px; height: 62px;
    background: var(--blue);
    border-top-left-radius: 10px;
    border-top-right-radius: 10px;
    display: flex; align-items: center; justify-content: center;
  }
</style>
</head>
<body>

  <section class="card card--front" aria-label="Vorderseite">
    <div class="wordmark">
      <span class="wordmark__square"></span>
      <span class="wordmark__name">ruhepol</span>
    </div>
  </section>

  <section class="card card--back" aria-label="Rückseite">
    <div class="person">
      <h1 class="person__name">Jonas Wendler</h1>
      <p class="person__role">Diplom-Psychologe, Heilpraktier für Psychotherapie<br>mit Spezialisierung Hypnose-Therapie</p>
    </div>

    <ul class="contacts">
      <li class="contacts__item">
        <span class="contacts__icon contacts__icon--pin">
          <svg width="14" height="16" viewBox="0 0 14 16"><path d="M7 1a5 5 0 0 0-5 5c0 3.5 5 9 5 9s5-5.5 5-9a5 5 0 0 0-5-5zm0 7a2 2 0 1 1 0-4 2 2 0 0 1 0 4z" fill="#fff"/></svg>
        </span>
        Ahornstraße 17 | 10405 Berlin
      </li>
      <li class="contacts__item">
        <span class="contacts__icon contacts__icon--mail">
          <svg width="18" height="13" viewBox="0 0 18 13"><rect x="1" y="1" width="16" height="11" fill="none" stroke="#fff" stroke-width="1.5"/><path d="M1 1l8 6 8-6" fill="none" stroke="#fff" stroke-width="1.5"/></svg>
        </span>
        info@ruhepol-hypnose.de
      </li>
      <li class="contacts__item">
        <span class="contacts__icon contacts__icon--web">
          <svg width="16" height="16" viewBox="0 0 16 16" fill="none" stroke="#fff" stroke-width="1.3"><circle cx="8" cy="8" r="6.5"/><ellipse cx="8" cy="8" rx="3" ry="6.5"/><path d="M1.5 8h13"/></svg>
        </span>
        www.ruhepol-hypnose.de
      </li>
      <li class="contacts__item">
        <span class="contacts__icon contacts__icon--tel"></span>
        Tel: 030 55 12 48 90
      </li>
    </ul>

    <div class="hotline">
      <span class="hotline__tab">
        <svg width="30" height="30" viewBox="0 0 24 24"><path d="M6.6 10.8a15 15 0 0 0 6.6 6.6l2.2-2.2a1 1 0 0 1 1-.25 11.4 11.4 0 0 0 3.6.57 1 1 0 0 1 1 1V20a1 1 0 0 1-1 1A17 17 0 0 1 3 4a1 1 0 0 1 1-1h3.5a1 1 0 0 1 1 1c0 1.25.2 2.45.57 3.57a1 1 0 0 1-.25 1z" fill="#fff"/></svg>
      </span>
      24-Std-AB: 030 31 87 22 06
    </div>
  </section>

</body>
</html>
```